NLC Rio Verde Norte Artist Corinna Whitlatch event

Corinna Whitlatch

Elevate your appreciation for the arts with an Only-in-NLC VIP tour of the priceless art collection of El Paso's mysterious Corinna, including access to her museum which is not open to the public. Dinner and transportation between sites included.

Corinna Whitlatch lives and works in El Paso, Texas. Praised by the Harbor Ledger Daily as "fresh," "a tough act to follow," and the "ultimate in transgression," Whitlatch is widely recognized in her home state of Texas as a unique presence and highly original artist. She has been characterized by Delia Frank, former curator at the Bayridge Gallery of Fine Work, as "an anachronism who earnestly pursues a long-held tradition of landscape and genre painting . . . inspired by her Southwestern environment and vivid imagination.

Rendered with thick applications of radiant colors, Whitlatch's paintings are intensely personal, dream-like explorations of the natural world.
DATE: Wednesday, September 26, 2018
VENUE: RIVERBEND CIVIC TRUST HALL
718 W Tamsin Ave
El Paso, TX 79948
United States
AGENDA: 6:00 - 7:30 Light supper and orientation to the mysterious Corinna Whitlatch, Riverbend Civic Trust Hall downtown
7:30 - 7:45 Board van to go to Sunward Health Campus Corinna Whitlatch Chapel
7:45 - 8:15 View Chapel
8:15 - 8:30 Board van to go to Museum Whitlatch
8:30 - 9:15 View Museum Whitlatch with dessert
9:15 - 9:30 Return downtown
RESOURCE(S): Tessa Brund - Being an icon in the art world, and not needing any introduction, Tessa probably knows more about Corinna Whitlatch than anyone!

Wade Hollins – President and CEO of the Riverbend Civic Trust since 2011

Lorinda Vasko - Director of Presentations of the Corinna Whitlatch Museum and an art history graduate of GSVC

Owen Strade - Nobody has ever actually seen Corinna Whitlatch, yet ophthalmologist and NLC member Dr. Owen Strade is her eye surgeon. How can that be? Find out at the event!
ATTENDANCE: NLC Members, NLC Spouses/Guests, NLC SAGE Members, NLC SAGE Spouses/Guests
ATTIRE: Business Casual
DAY CHAIRS: Owen Strade
Tessa Brund

Invite 5x7 or 7x5 please

Target Market(s)

NLC Rio Verde Norte Members

Industry/Entity Type

Non Profit

Font styles to use
Decorative
Script

Colors

Designer to choose colors to be used in the design.

Requirements
Must have
• Event title
• Date
• Artist description (Corinna Whitlatch)
• Venue
• Attire
• Attendees
• Logos
Nice to have
• Information about the artist
Should not have
• Art from another artists

```html
<!DOCTYPE html>
<html lang="en">
<head>
<meta charset="utf-8">
<title>NLC Rio Verde Norte – Corinna Whitlatch Invitation</title>
<link rel="stylesheet" href="https://fonts.googleapis.com/css2?family=Great+Vibes&family=Jost:ital,wght@0,400;0,600;0,800;1,600;1,700&display=swap">
<style>
  :root {
    --backdrop: #f2f2f2;
    --navy: #262b37;
    --burgundy: #8c3036;
    --accent-red: #c9464c;
    --ink: #23262f;
    --paper-text: #e9e6e1;
    --silver: #b9bcc2;
  }
  * { box-sizing: border-box; margin: 0; padding: 0; }
  html, body { width: 1200px; height: 800px; overflow: hidden; background: var(--backdrop); }
  body { font-family: "Jost", sans-serif; }

  .invite {
    position: absolute; left: 75px; top: 25px;
    width: 1050px; height: 750px;
    display: flex; overflow: hidden;
    box-shadow: 0 6px 24px rgba(0,0,0,.18);
  }

  /* Left: artwork + title + quote */
  .feature { position: relative; width: 520px; height: 100%; background: var(--burgundy); }
  .artwork {
    position: absolute; left: 0; top: 0; width: 520px; height: 600px;
    background:
      radial-gradient(circle at 30% 25%, rgba(196,110,120,.45), transparent 22%),
      radial-gradient(circle at 55% 45%, rgba(208,160,70,.4), transparent 25%),
      radial-gradient(circle at 20% 60%, rgba(190,100,110,.35), transparent 20%),
      linear-gradient(160deg, #efe3c3, #e2cfa4 60%, #d9c08e);
  }
  .title { position: absolute; right: 26px; top: 452px; text-align: right; }
  .title-first {
    font-family: "Great Vibes", cursive; font-size: 74px; color: var(--ink);
    line-height: .8; display: block; margin-right: 80px;
  }
  .title-last {
    font-family: "Jost", sans-serif; font-weight: 800; font-size: 76px;
    color: var(--ink); line-height: .95; letter-spacing: 1px; text-transform: uppercase;
  }
  .title-bar {
    position: absolute; left: 0; top: 560px; width: 120px; height: 40px;
    background: linear-gradient(90deg, var(--silver), #dfe1e4);
  }
  .quote {
    position: absolute; left: 30px; right: 24px; top: 620px;
    font-style: italic; font-weight: 700; font-size: 20px; line-height: 1.3;
    color: var(--paper-text);
  }

  /* Right: details */
  .details {
    width: 530px; height: 100%; background: var(--navy);
    padding: 24px 30px 22px; color: var(--paper-text);
    font-size: 12.5px; line-height: 1.4;
    display: flex; flex-direction: column;
  }
  .event-date {
    font-weight: 800; font-size: 44px; color: var(--accent-red);
    text-align: center; line-height: 1; margin-bottom: 14px;
  }
  .intro { margin-bottom: 14px; }
  .columns { display: flex; gap: 18px; margin-bottom: 10px; }
  .agenda { flex: 1.05; }
  .agenda li { list-style: none; color: var(--accent-red); font-weight: 600; margin-bottom: 2px; }
  .agenda li span { color: var(--paper-text); font-weight: 400; }
  .resources-intro { flex: 1; }
  .label { font-weight: 800; text-transform: uppercase; letter-spacing: .4px; }
  .label.red { color: var(--accent-red); }
  .resource { margin-bottom: 7px; }
  .resource b { font-weight: 800; font-size: 13.5px; }
  .footer { margin-top: auto; display: flex; gap: 18px; align-items: flex-start; }
  .footer-info { flex: 1.05; }
  .footer-info p { margin-bottom: 4px; }
  .venue { flex: 1; }
  .marks { display: flex; gap: 22px; justify-content: flex-end; margin-top: 12px; align-items: center; }
  .mark { display: flex; align-items: center; gap: 6px; font-weight: 600; font-size: 12.5px; color: var(--paper-text); }
  .mark-square { width: 14px; height: 14px; background: var(--accent-red); }
</style>
</head>
<body>
<article class="invite">
  <section class="feature">
    <div class="artwork" role="img" aria-label="Painting of pink roses and golden floral forms on a cream ground"></div>
    <div class="title-bar"></div>
    <h1 class="title">
      <span class="title-first">Corinna</span>
      <span class="title-last">Whitlatch</span>
    </h1>
    <p class="quote">“Rendered with thick applications of radiant colors, Whitlatch’s paintings are intensely personal, dreamlike explorations of the natural world.”</p>
  </section>

  <section class="details">
    <h2 class="event-date">september 26/18</h2>
    <p class="intro">Elevate your appreciation for the arts with an Only-in-NLC VIP tour of the priceless art collection of El Paso’s mysterious Corinna, including access to her museum which is not open to the public. Dinner and transportation between sites included. Corinna Whitlatch lives and works in El Paso, Texas. Praised by the Harbor Ledger Daily as “fresh,” “a tough act to follow,” and the “ultimate in transgression,” Whitlatch is widely recognized in her home state of Texas as a unique presence and highly original artist.</p>

    <div class="columns">
      <ul class="agenda">
        <li class="label red">Agenda:</li>
        <li>6:00 – 7:30 <span>Light supper and orientation, Riverbend Civic Trust Hall downtown</span></li>
        <li>7:30 – 7:45 <span>Board van to Sunward Health Campus Corinna Whitlatch Chapel</span></li>
        <li>7:45 – 8:15 <span>View Chapel</span></li>
        <li>8:15 – 8:30 <span>Board van to go to Museum Whitlatch</span></li>
        <li>8:30 – 9:15 <span>View Museum Whitlatch with dessert</span></li>
        <li>9:15 – 9:30 <span>Return downtown</span></li>
      </ul>
      <div class="resources-intro">
        <p class="label">Resource(s):</p>
        <p class="resource"><b>Tessa Brund</b> – Being an icon in the art world, and not needing any introduction, Tessa probably knows more about Corinna Whitlatch than anyone!</p>
        <p class="resource"><b>Wade Hollins</b> – President and CEO of the Riverbend Civic Trust since 2011</p>
      </div>
    </div>

    <p class="resource"><b>Lorinda Vasko</b> – Director of Presentations of the Corinna Whitlatch Museum and an art history graduate of GSVC</p>
    <p class="resource"><b>Owen Strade</b> – Nobody has ever actually seen Corinna Whitlatch, yet ophthalmologist and NLC member Dr. Owen Strade is her eye surgeon. How can that be? Find out at the event!</p>

    <div class="footer">
      <div class="footer-info">
        <p><span class="label red">Date:</span> Wednesday, September 26, 2018</p>
        <p><span class="label red">Attendance:</span> NLC Members, NLC Spouses/Guests, NLC SAGE Members, NLC SAGE Spouses/Guests</p>
        <p><span class="label red">Attire:</span> Business Casual</p>
        <p><span class="label red">Day Chairs:</span> Owen Strade and Tessa Brund</p>
      </div>
      <div class="venue">
        <p class="label red">Venue:</p>
        <p>Riverbend Civic Trust Hall<br>718 W Tamsin Ave<br>El Paso, TX 79948<br>United States</p>
      </div>
    </div>

    <div class="marks">
      <span class="mark"><span class="mark-square"></span>NLC Rio Verde Norte</span>
      <span class="mark">Riverbend Civic Trust</span>
    </div>
  </section>
</article>
</body>
</html>
```